Kelpline Aquatics Website and inner template.

New website design for an existing client. Need a home page design and a simplified inner page template design, I have included a txt document with the specifics for this website design/poject. I have copy and pasted the info below
Project Description: Website design ( home page with an inner page template ) for Kelpline Aquatics LLC
Current Website Address: https://kelplineaquatics.example
Main navigation link: ( same as on current website with the exception of Links and Resources being removed )
Instruction/Courses
Rentals
Trips & Charters
Service & Repairs
Tank Fills
Home
Contact
About ( Company Info )
Events
Specials
Home page specifics:
As with all website lately, they requested a large "hero banner" or "slider image" above the fold just below the navigation. Examples
https://harrowmetalworks.example/
https://pinfernstudio.example/
https://lomasparrowfield.example/
In addition to the main navigation menu and hero banner, we need to highlight some important features/links on the home page
Social media icons for facebook and instagram
Store Hours
Contact Information in cluding phone numbers
Scuba Instruction/Courses Link highlight area
Scuba Rental Gear Link highlight area
Scuba Repair Service Link highlight area
Large content area. Needs to be large enoug to move over the existing content on the current website ( see link above )
Large section for "Snorkels, Masks, Fins - How to Fit & Care for them " . Currently that is the only page on the resources page. Since we are removing the resources page, we would like make this a stand alone page only accessible via the home page in a highlight area.
Other Notes:
I have attached the logo to the project.
IMPORTANT... ONLY USE GRAPHICS/IMAGES from plenta image. ( https://www.plentaimage.example/ ) This is important because we have an account with them so you can use the watermarked images then when I build the website I can easily purchase the licensing rights for those images. You dont' need an account to do searches, locate images and use the water marked image in the design.
Target Market(s)
Diving Lessons, Equipment repair and charters
Number of Pages Required
2 page
Requirements
Must have
- Please see attached txt document with all the project specifics
Nice to have
Should not have

```html
<!DOCTYPE html>
<html lang="en">
<head>
<meta charset="utf-8">
<title>Kelpline Aquatics LLC – Scuba Equipment Repair & Diving Shop</title>
<link rel="stylesheet" href="https://fonts.googleapis.com/css2?family=Montserrat:wght@400;500;600;700;800&display=swap">
<style>
:root{
  --red:#d7222a;
  --red-dark:#a3141b;
  --pink:#f6c3c5;
  --ink:#222222;
  --text:#4a4a4a;
  --grey-bar:#e9e9e9;
  --line:#cfcfcf;
  --white:#ffffff;
  --font:'Montserrat', Arial, sans-serif;
}
*{box-sizing:border-box;margin:0;padding:0}
html,body{width:1200px;height:4796px;overflow:hidden;background:var(--white)}
body{font-family:var(--font);color:var(--text)}
.page{position:relative;width:1200px;height:4796px;overflow:hidden}
.abs{position:absolute}
a{color:inherit;text-decoration:none}
.btn{position:absolute;display:flex;align-items:center;justify-content:center;background:var(--red);color:var(--white);font-weight:700;font-size:13px;letter-spacing:.5px;border-radius:23px;text-transform:uppercase}
.photo{position:absolute}

/* top bar */
.topbar{position:absolute;left:0;top:0;width:1200px;height:52px;background:var(--grey-bar)}
.toplinks{position:absolute;left:111px;top:18px;display:flex;gap:30px;font-size:11.5px;font-weight:500;color:var(--ink)}
.callbox{position:absolute;left:735px;top:0;width:353px;height:60px}
.callbox svg{position:absolute;left:0;top:0}
.call-icon{position:absolute;left:30px;top:10px;width:38px;height:38px;border:2px solid var(--white);border-radius:50%}
.call-lines{position:absolute;left:92px;top:5px;color:var(--white)}
.call-lines .main{font-size:20px;font-weight:600;line-height:24px}
.call-lines .toll{font-size:14px;font-weight:600;line-height:20px}

/* header */
.brand{position:absolute;left:111px;top:70px;display:flex;align-items:center;gap:12px}
.brand-square{width:44px;height:44px;background:var(--red)}
.brand-name{font-weight:700;font-size:27px;color:var(--red);letter-spacing:-.3px}
.mainnav{position:absolute;top:90px;font-size:13.5px;font-weight:500;color:var(--ink)}
.mainnav.active{color:var(--red)}
.nav-marker{position:absolute;left:643px;top:119px;width:0;height:0;border-left:10px solid transparent;border-right:10px solid transparent;border-bottom:15px solid var(--red)}

/* hero */
.hero{position:absolute;left:0;top:134px;width:1200px;height:595px;background:linear-gradient(120deg,#0a2f55 0%,#11508c 40%,#1e6b9e 60%,#b4744a 85%,#d18a45 100%)}
.hero-title{position:absolute;left:108px;top:265px;font-size:53px;line-height:51px;font-weight:800;color:var(--white);width:620px}
.hero-arrow{position:absolute;top:398px}
.feature{position:absolute;top:571px;width:316px;height:322px}
.feature-band{position:absolute;left:0;top:121px;width:316px;height:80px;background:rgba(255,255,255,.78);display:flex;align-items:center;justify-content:center;color:var(--red);font-size:19px;font-weight:500;letter-spacing:.3px}

/* welcome */
.section-title{position:absolute;font-size:34px;font-weight:700;color:var(--ink);letter-spacing:.5px;white-space:nowrap}
.section-title span{color:var(--red)}
.section-title.about-title{font-size:30px}
.copy{position:absolute;font-size:12.6px;line-height:22.2px;color:var(--text)}

/* red band */
.band{position:absolute;left:0;top:1420px}
.framed-photo{position:absolute;left:604px;top:1343px;width:485px;height:342px;border:5px solid var(--white);background:linear-gradient(135deg,#d07a2a 0%,#c86b22 25%,#1b6d9e 50%,#0f4e86 100%)}
.work-title{position:absolute;left:0;top:1768px;width:1200px;text-align:center;font-size:35px;font-weight:600;color:var(--white);letter-spacing:1px}
.work-card{position:absolute;top:1884px;width:310px;height:270px;background:var(--white)}
.work-photo{position:absolute;top:1841px;width:280px;height:209px}
.work-name{position:absolute;top:2064px;width:310px;text-align:center;font-size:19px;line-height:26px;font-weight:500;color:var(--ink)}
.work-text{position:absolute;top:2124px;width:310px;text-align:center;font-size:12.6px;line-height:22.2px;color:var(--text);padding:0 28px}

/* about */
.about-frame{position:absolute;left:95px;top:2396px;width:463px;height:381px;border:2.5px solid var(--red)}
.about-photo{position:absolute;left:112px;top:2377px;width:465px;height:385px;background:linear-gradient(160deg,#5fd0d8 0%,#2fa9c4 40%,#8fd3cf 75%,#d7ecdd 100%)}
.about-sub{position:absolute;left:620px;top:2428px;font-size:16px;font-weight:600;color:var(--ink);letter-spacing:.3px}

/* guide */
.guide{position:absolute;left:0;top:2859px;width:1200px;height:378px;background:linear-gradient(180deg,#0d4f9c 0%,#1463b8 55%,#0d55a6 100%)}
.guide-title{position:absolute;left:0;top:2940px;width:1200px;text-align:center;font-size:34px;line-height:52px;font-weight:700;color:var(--white);letter-spacing:.8px}
.guide-text{position:absolute;left:0;top:3052px;width:1200px;text-align:center;font-size:14.5px;font-weight:500;color:var(--white)}

/* partners */
.partners-title{position:absolute;left:0;top:3325px;width:1200px;text-align:center;font-size:34px;font-weight:500;color:var(--ink);letter-spacing:.5px}
.partner-row{position:absolute;left:112px;top:3408px;width:976px;height:84px;border:1px solid var(--line);display:flex}
.partner{flex:1;border-right:1px solid var(--line);display:flex;align-items:center;justify-content:center;font-size:19px;font-weight:700;color:var(--ink)}
.partner:last-child{border-right:none}
.carousel-btn{position:absolute;top:3433px;width:34px;height:34px;border-radius:50%}

/* contact */
.contact-title{position:absolute;left:0;top:3580px;width:1200px;text-align:center;font-size:34px;font-weight:500;color:var(--ink);letter-spacing:.5px}
.contact-sub{position:absolute;left:0;top:3638px;width:1200px;text-align:center;font-size:13.5px;color:var(--text)}
.info{position:absolute;top:3701px;width:240px;text-align:center}
.info-icon{width:64px;height:64px;margin:0 auto;border:2.5px solid var(--red);border-radius:50%;display:flex;align-items:center;justify-content:center}
.info-label{margin-top:14px;font-size:13px;font-weight:600;color:var(--ink);letter-spacing:.5px}
.info-value{font-size:13px;line-height:21px;color:var(--text)}
.field{position:absolute;background:#f4f4f4;border:1px solid #bdbdbd;font-size:12.5px;color:#777;padding-left:22px;display:flex;align-items:center}
.field.msg{align-items:flex-start;padding-top:16px}

/* footer */
.footer-bg{position:absolute;left:0;top:4330px}
.foot-brand{position:absolute;left:149px;top:4507px;width:256px;height:42px;background:var(--white);display:flex;align-items:center;gap:8px;padding-left:10px}
.foot-brand .sq{width:24px;height:24px;background:var(--red)}
.foot-brand .nm{font-size:17.5px;font-weight:700;color:var(--red);white-space:nowrap}
.foot-h{position:absolute;font-size:17px;font-weight:700;color:var(--white)}
.foot-line{position:absolute;font-size:12.5px;color:var(--white)}
.foot-link{position:absolute;font-size:12.5px;color:var(--white)}
.foot-link::before{content:"»";margin-right:12px;font-weight:700}
.social{position:absolute;top:4557px;width:42px;height:42px;border:1.5px solid var(--white);background:rgba(255,255,255,.08)}
.social i{position:absolute;left:15px;top:15px;width:9px;height:9px;background:var(--white);border-radius:50%}
.divider{position:absolute;left:0;top:4715px;width:1200px;border-top:1.5px dashed rgba(255,255,255,.75)}
.goup{position:absolute;left:1008px;top:4699px;width:80px;height:20px;border-radius:10px;background:var(--white);color:var(--red);font-size:10.5px;font-weight:700;display:flex;align-items:center;justify-content:center}
.copyright{position:absolute;left:0;top:4744px;width:1200px;text-align:center;font-size:12px;color:var(--white)}
</style>
</head>
<body>
<div class="page">

  <header>
    <div class="topbar"></div>
    <nav class="toplinks" aria-label="Services">
      <a href="#">Instruction/Courses</a>
      <a href="#">Rentals</a>
      <a href="#">Trips &amp; Charters</a>
      <a href="#">Service &amp; Repairs</a>
      <a href="#">Tank Fills</a>
    </nav>
    <div class="callbox">
      <svg width="353" height="60" viewBox="0 0 353 60"><polygon points="14,0 353,0 339,60 0,60" fill="#d7222a"/></svg>
      <div class="call-icon">
        <svg width="34" height="34" viewBox="0 0 34 34"><path d="M12 9c1 0 2 3 2 4s-2 2-2 3c1 3 3 5 6 6 1 0 2-2 3-2s4 1 4 2c0 2-2 4-4 4-7 0-13-6-13-13 0-2 2-4 4-4z" fill="#fff"/><path d="M20 8a7 7 0 0 1 6 6M20 12a3 3 0 0 1 2 2" stroke="#fff" stroke-width="1.6" fill="none"/></svg>
      </div>
      <div class="call-lines">
        <div class="main">(555) 014-2290</div>
        <div class="toll">TOLL FREE (800) 555-0187</div>
      </div>
    </div>

    <a class="brand" href="#"><span class="brand-square"></span><span class="brand-name">KELPLINE AQUATICS, LLC</span></a>
    <a class="mainnav active" style="left:633px" href="#">HOME</a>
    <a class="mainnav" style="left:718px" href="#">CONTACT</a>
    <a class="mainnav" style="left:829px" href="#">ABOUT</a>
    <a class="mainnav" style="left:921px" href="#">EVENTS</a>
    <a class="mainnav" style="left:1019px" href="#">SPECIALS</a>
    <div class="nav-marker"></div>
  </header>

  <section>
    <div class="hero" role="img" aria-label="Two scuba divers swimming over a colourful coral reef"></div>
    <h1 class="hero-title">Full Service Scuba Equipment Repair &amp; Scuba Diving Shop</h1>
    <a class="btn" href="#" style="left:112px;top:443px;width:164px;height:44px">Get Started</a>
    <svg class="hero-arrow" style="left:44px" width="30" height="60" viewBox="0 0 30 60"><polyline points="26,4 4,30 26,56" fill="none" stroke="#fff" stroke-width="2.5"/></svg>
    <svg class="hero-arrow" style="left:1126px" width="30" height="60" viewBox="0 0 30 60"><polyline points="4,4 26,30 4,56" fill="none" stroke="#fff" stroke-width="2.5"/></svg>

    <div class="feature" style="left:112px">
      <div class="photo" role="img" aria-label="Diver beside pink sea fans" style="left:0;top:0;width:316px;height:322px;background:linear-gradient(180deg,#1b7dbb 0%,#2a6aa0 35%,#c2426a 70%,#d85a86 100%)"></div>
      <div class="feature-band">RESCUE &amp; COMMERCIAL</div>
    </div>
    <div class="feature" style="left:441px">
      <div class="photo" role="img" aria-label="Diver exploring an underwater cave lit by sun rays" style="left:0;top:0;width:316px;height:322px;background:linear-gradient(180deg,#0b2d3d 0%,#2f8aa5 40%,#1a6b8c 70%,#0d3a4e 100%)"></div>
      <div class="feature-band">SCUBA &amp; EXOTIC TRAVEL</div>
    </div>
    <div class="feature" style="left:770px">
      <div class="photo" role="img" aria-label="Schooling fish over a shallow reef" style="left:0;top:0;width:318px;height:322px;background:linear-gradient(180deg,#1352b0 0%,#1b6ccc 40%,#5a8aa0 70%,#a78a6a 100%)"></div>
      <div class="feature-band">SNORKELING &amp; SWIMMING</div>
    </div>
  </section>

  <section>
    <h2 class="section-title" style="left:112px;top:980px">WELCOME TO <span>KELPLINE AQUATICS</span></h2>
    <p class="copy" style="left:112px;top:1040px;width:800px">Welcome to Kelpline Aquatics, a scuba and snorkeling shop located in the beautiful town of Millbrook Connecticut, in Harbor Row Plaza which is across the street from The Millbrook Rail Depot. Kelpline Aquatics has been servicing the scuba, snorkeling, spearfishing, and swimming communities for over 35 years! We carry a full line of equipment for your underwater adventures - from mask, fins, and snorkels to tanks, regulators, and suits. We have swim goggles and fins; spearfishing guns, bands, tips, and accessories; bags to carry your equipment; dive watches and computers; full face masks and books to read; and all types of equipment for the technical and rescue diver! Kelpline Aquatics offers instruction for scuba diving, from entry level up to instructor preparation and for dive rescue teams. We also offer technical diving classes from basic nitrox to advanced decompression classes. Check out our CALENDAR for courses and starting dates. Our teaching staff is hand-picked to provide the best instruction to make you a comfortable and safe diver, while having fun doing so!</p>
    <a class="btn" href="#" style="left:112px;top:1291px;width:164px;height:45px">Learn More</a>
  </section>

  <section>
    <svg class="band" width="1200" height="712" viewBox="0 1420 1200 712">
      <defs>
        <linearGradient id="sea" x1="0" y1="0" x2="0" y2="1">
          <stop offset="0" stop-color="#d7222a"/>
          <stop offset="0.45" stop-color="#d7222a"/>
          <stop offset="0.62" stop-color="#9e1219"/>
          <stop offset="0.8" stop-color="#c21c24"/>
          <stop offset="1" stop-color="#d7222a"/>
        </linearGradient>
      </defs>
      <polygon points="0,1562 363,1434 1200,1620 1200,1700 0,1700" fill="#f6c3c5"/>
      <polygon points="0,1562 363,1462 1088,1525 1200,1560 1200,2132 0,2132" fill="url(#sea)"/>
    </svg>
    <div class="framed-photo" role="img" aria-label="Diver swimming past an orange sea fan on a blue reef"></div>

    <h2 class="work-title">OUR WORK</h2>

    <div class="work-card" style="left:112px"></div>
    <div class="work-photo" style="left:127px;background:linear-gradient(180deg,#1a78c8 0%,#1d8fd0 50%,#5a9a9a 100%)" role="img" aria-label="Diver swimming alongside a sea turtle"></div>
    <div class="work-name" style="left:112px">Scuba Instruction/<br>Courses</div>
    <p class="work-text" style="left:112px">From the North Atlantic lobster off of the coast of New England to the hand-tamed stingrays at Ray Lagoon in the Coral Keys</p>
    <a class="btn" href="#" style="left:185px;top:2232px;width:164px;height:45px">Read More</a>

    <div class="work-card" style="left:445px"></div>
    <div class="work-photo" style="left:460px;background:linear-gradient(180deg,#8fc1dc 0%,#c8d8dc 35%,#3c4f6a 65%,#5a4a3c 100%)" role="img" aria-label="Scuba mask and fins resting on a beach rock"></div>
    <div class="work-name" style="left:445px">Scuba Rental<br>Gear</div>
    <p class="work-text" style="left:445px">Kelpline Aquatics has a full line of scuba equipment available for rental. Just because you haven't purchased your own</p>
    <a class="btn" href="#" style="left:518px;top:2232px;width:164px;height:45px">Read More</a>

    <div class="work-card" style="left:778px"></div>
    <div class="work-photo" style="left:793px;background:linear-gradient(180deg,#5a2a22 0%,#c9b8a8 45%,#7a7a7a 75%,#333 100%)" role="img" aria-label="Technician's hands assembling a regulator on a tank"></div>
    <div class="work-name" style="left:778px">Scuba Repair<br>Service</div>
    <p class="work-text" style="left:778px">Kelpline Aquatics has well trained certified technicians ready to service your scuba equipment for all divers, including sport divers</p>
    <a class="btn" href="#" style="left:851px;top:2232px;width:164px;height:45px">Read More</a>
  </section>

  <section>
    <div class="about-frame"></div>
    <div class="about-photo" role="img" aria-label="Snorkeler swimming beside a stingray over white sand"></div>
    <h2 class="section-title about-title" style="left:620px;top:2370px">ABOUT <span>KELPLINE AQUATICS</span></h2>
    <div class="about-sub">CT SCUBA REPAIR SHOP &amp; SCUBA DIVING SHOP</div>
    <p class="copy" style="left:620px;top:2470px;width:468px;text-align:justify">Kelpline Aquatics began on August 23, 1981 when Tom Berrigan became a DiveCert instructor. Tom started teaching scuba classes and selling diving equipment out of the back of his van. He then set up his first dive shop in the basement of his house in Alder Falls Connecticut. In 1986 Kelpline Aquatics opened up in a storefront in Greyport Connecticut. The business continued to grow, and in 1991 Tom bought Hal Dunmore's scuba business, Tidewater Divers in North Fenwick, and moved to our current location at Harbor Row Plaza in Millbrook Connecticut, across from the Millbrook Rail Depot. The dive shop has expanded to 3 store fronts since the initial move there.</p>
    <a class="btn" href="#" style="left:620px;top:2710px;width:164px;height:45px">Read More</a>
  </section>

  <section>
    <div class="guide" role="img" aria-label="Diver in fins swimming near a shipwreck in deep blue water"></div>
    <h2 class="guide-title">SNORKELS, MASKS, FINS - HOW TO FIT<br>&amp; CARE FOR THEM</h2>
    <p class="guide-text">Learn how to fit your snorkel/scuba mask and how to care &amp; maintain your mask, snorkel &amp; fins.</p>
    <a class="btn" href="#" style="left:525px;top:3097px;width:164px;height:45px">Read More</a>
  </section>

  <section>
    <h2 class="partners-title">Scuba Links &amp; Diving Websites</h2>
    <div class="partner-row">
      <div class="partner">Lumara</div>
      <div class="partner">Brackett</div>
      <div class="partner">Tidecraft</div>
      <div class="partner">Bluefin Gear</div>
      <div class="partner">Sealtide</div>
    </div>
    <svg class="carousel-btn" style="left:92px" viewBox="0 0 34 34"><circle cx="17" cy="17" r="16" fill="#e4e4e4"/><polyline points="19,12 14,17 19,22" fill="none" stroke="#555" stroke-width="2"/></svg>
    <svg class="carousel-btn" style="left:1072px" viewBox="0 0 34 34"><circle cx="17" cy="17" r="16" fill="#d7222a"/><polyline points="15,12 20,17 15,22" fill="none" stroke="#fff" stroke-width="2"/></svg>
  </section>

  <section>
    <h2 class="contact-title">CONTACT US</h2>
    <p class="contact-sub">Lorem ipsum dolor sit amet, consectetur adipiscing elit, sed do eiusmod</p>

    <div class="info" style="left:246px">
      <div class="info-icon"><svg width="22" height="28" viewBox="0 0 22 28"><path d="M11 1a9 9 0 0 1 9 9c0 7-9 17-9 17S2 17 2 10a9 9 0 0 1 9-9z" fill="none" stroke="#d7222a" stroke-width="2.4"/><circle cx="11" cy="10" r="3.2" fill="#d7222a"/></svg></div>
      <div class="info-label">ADDRESS :</div>
      <div class="info-value">12 Harbor Row, Millbrook, CT<br>06000</div>
    </div>
    <div class="info" style="left:486px">
      <div class="info-icon"><svg width="24" height="24" viewBox="0 0 24 24"><path d="M6 2c1 0 3 4 3 5s-2 2-2 3c1 3 4 6 7 7 1 0 2-2 3-2s5 2 5 3c0 2-2 4-4 4C9 22 2 15 2 6c0-2 2-4 4-4z" fill="#d7222a"/></svg></div>
      <div class="info-label">PHONE :</div>
      <div class="info-value">(555) 014-2290</div>
    </div>
    <div class="info" style="left:726px">
      <div class="info-icon"><svg width="26" height="20" viewBox="0 0 26 20"><rect x="1" y="1" width="24" height="18" rx="2" fill="#d7222a"/><polyline points="2,3 13,11 24,3" fill="none" stroke="#fff" stroke-width="2"/></svg></div>
      <div class="info-label">EMAIL :</div>
      <div class="info-value">info@kelplineaquatics.example</div>
    </div>

    <form>
      <div class="field" style="left:238px;top:3863px;width:352px;height:56px">First name</div>
      <div class="field" style="left:608px;top:3863px;width:352px;height:56px">Last name</div>
      <div class="field" style="left:238px;top:3938px;width:352px;height:57px">Phone</div>
      <div class="field" style="left:608px;top:3938px;width:352px;height:57px">Email address</div>
      <div class="field msg" style="left:238px;top:4016px;width:722px;height:134px">Message</div>
      <div class="btn" style="left:521px;top:4172px;width:158px;height:48px">Submit</div>
    </form>
  </section>

  <footer>
    <svg class="footer-bg" width="1200" height="466" viewBox="0 4330 1200 466">
      <polygon points="0,4447 623,4349 1200,4420 1200,4452" fill="#f6c3c5"/>
      <polygon points="0,4450 623,4368 1200,4446 1200,4796 0,4796" fill="#d7222a"/>
    </svg>

    <div class="foot-brand"><span class="sq"></span><span class="nm">KELPLINE AQUATICS, LLC</span></div>
    <div class="foot-h" style="left:149px;top:4570px">Store Hours</div>
    <svg class="abs" style="left:151px;top:4608px" width="14" height="14" viewBox="0 0 14 14"><circle cx="7" cy="7" r="6" fill="none" stroke="#fff" stroke-width="1.6"/><polyline points="7,3.5 7,7 9.5,8.5" fill="none" stroke="#fff" stroke-width="1.4"/></svg>
    <div class="foot-line" style="left:179px;top:4607px">Mon - Sat</div>
    <div class="foot-line" style="left:179px;top:4633px">10am to 6pm</div>
    <div class="foot-line" style="left:179px;top:4659px">Closed on Sun</div>

    <div class="foot-h" style="left:500px;top:4507px">Links</div>
    <a class="foot-link" href="#" style="left:502px;top:4560px">Instruction/Courses</a>
    <a class="foot-link" href="#" style="left:502px;top:4586px">Rentals</a>
    <a class="foot-link" href="#" style="left:502px;top:4612px">Trips &amp; Charters</a>
    <a class="foot-link" href="#" style="left:502px;top:4638px">Service &amp; Repairs</a>
    <a class="foot-link" href="#" style="left:502px;top:4664px">Tank Fills</a>
    <a class="foot-link" href="#" style="left:690px;top:4560px">Home</a>
    <a class="foot-link" href="#" style="left:690px;top:4586px">Contact</a>
    <a class="foot-link" href="#" style="left:690px;top:4612px">About</a>
    <a class="foot-link" href="#" style="left:690px;top:4638px">Events</a>
    <a class="foot-link" href="#" style="left:690px;top:4664px">Specials</a>

    <div class="foot-h" style="left:839px;top:4507px">Connect With Us</div>
    <a class="social" href="#" aria-label="Social profile" style="left:843px"><i></i></a>
    <a class="social" href="#" aria-label="Social profile" style="left:893px"><i></i></a>
    <a class="social" href="#" aria-label="Social profile" style="left:943px"><i></i></a>
    <a class="social" href="#" aria-label="Social profile" style="left:993px"><i></i></a>

    <div class="divider"></div>
    <a class="goup" href="#">&#8593; Go Up</a>
    <p class="copyright">© 2021 Company name | All Rights Reserved</p>
  </footer>

</div>
</body>
</html>
```